Photography Prints Business Card Design

Background info: Nature, flower, landscape,  macro, wildlife photographer. Shoot color and B&W images. Sell prints at juried fine art shows.
Looking for two-sided, clean, memorable design with creative use of my initials, DH.   I like the DH symbol in the my logo. Just use the DH symbol. Do not leave the underlying text as uploaded by me. I do not like the serif font and positioning of the words!  Either  remove the small print "Dorian Hallet Photography" under the logo,  or change to a sans serif font, or reposition with "Dorian Hallet" above "Photography" which seems to work with serif fonts.
Target Market(s)
Sophisticated art buyers, post-college to middle age
Industry/Entity Type
Business
Contact Information for Business Card
Dorian Hallet Photography
728 Maple Brook CT
Cedar Hollow, NC 28999
(555) 555-0148
www.dorianhallet.com
CP:halletphoto
dorian@dorianhallet.com
If using just one line address, make sure there is a comma after  "CT" in street address. For example:
728 Maple Brook CT, Cedar Hollow, NC 28999
Requirements
Must have
- 1.Two-sided card submitted as one design.
2. Must use the DH symbol in my logo.
3. Do not leave the text "Dorian Hallet Photography" under the DH symbol in the logo uploaded by me. I do not like that serif font or the positioning of the words! Either remove the small print "Dorian Hallet Photography" under the logo entirely, or change text to a sans serif font, or reposition text with "Dorian Hallet" above "Photography" which seems to work with serif fonts.
Nice to have
- Can use my DH logo (three file types uploaded: AI, PSD, TIF)  I  like the attached B&W water droplet photo.  My pictures on my website, www.dorianhhallet.com  can also be used.  Possible use of Chirply logo with (either the "f" alone or the square blue icon with white "f") my CP page short url name: halletphoto.
Should not have
- 1.No icons or pictures  of camera or lenses or other photographic gear or film strips.
2. No QR or other "barcode" type symbols.
3. No outlining of my logo symbol (drop shadow possibly).
4. No decorative or outlined fonts.
5. I am not a fan of most script fonts.
6. No play on "Hallet" such as snow or other winter season symbols.
7. Do not keep the original text, "Dorian Hallet Photography" under DH logo. Change it or remove it entirely.

```html
<!DOCTYPE html>
<html lang="en">
<head>
<meta charset="utf-8">
<title>Dorian Hallet Photography – Business Card</title>
<link rel="stylesheet" href="https://fonts.googleapis.com/css2?family=Raleway:wght@200;300;400&display=swap">
<style>
  :root {
    --stage: #e8e6e2;
    --ink-black: #0a0a0a;
    --ink-dark: #1c1c1c;
    --ink-mid: #6d6d6d;
    --paper-white: #ffffff;
    --text-soft: #e6e6e6;
    --shadow: rgba(0, 0, 0, 0.22);
  }
  * { margin: 0; padding: 0; box-sizing: border-box; }
  html, body {
    width: 1200px;
    height: 900px;
    overflow: hidden;
    background: var(--stage);
    font-family: "Raleway", sans-serif;
    font-weight: 300;
  }
  .card {
    position: absolute;
    left: 270px;
    width: 660px;
    height: 377px;
    border-radius: 18px;
    overflow: hidden;
    box-shadow: 0 10px 28px var(--shadow);
  }
  .card-front { top: 56px; }
  .card-back { top: 467px; }

  /* Front */
  .droplet-photo {
    position: absolute;
    inset: 0;
    background:
      radial-gradient(ellipse at 62% 30%, #d9d9d9 0%, #a9a9a9 38%, transparent 70%),
      linear-gradient(100deg, var(--ink-black) 0%, #2a2a2a 18%, #8f8f8f 34%, #c4c4c4 60%, #9a9a9a 100%);
  }
  .front-monogram {
    position: absolute;
    right: 54px;
    top: 92px;
    font-size: 120px;
    line-height: 1;
    letter-spacing: -4px;
    color: var(--ink-black);
  }

  /* Back */
  .back-surface {
    position: absolute;
    inset: 0;
    background:
      linear-gradient(118deg, transparent 44%, rgba(255,255,255,0.10) 52%, transparent 62%),
      linear-gradient(100deg, var(--ink-black) 0%, var(--ink-dark) 38%, #3f3f3f 62%, var(--ink-mid) 100%);
  }
  .back-monogram {
    position: absolute;
    left: 38px;
    top: 128px;
    font-size: 118px;
    line-height: 1;
    letter-spacing: -4px;
    color: var(--paper-white);
  }
  .studio-name {
    position: absolute;
    left: 236px;
    top: 30px;
    color: var(--text-soft);
    font-size: 40px;
    font-weight: 200;
    line-height: 46px;
    letter-spacing: 2px;
    text-transform: uppercase;
    white-space: nowrap;
  }
  .studio-name .line-one,
  .studio-name .line-two { display: block; }
  .studio-name .line-two { padding-left: 40px; }
  .contact-list {
    position: absolute;
    right: 22px;
    top: 142px;
    list-style: none;
    text-align: right;
    color: var(--text-soft);
    font-size: 15px;
    letter-spacing: 0.5px;
    text-transform: uppercase;
  }
  .contact-list li {
    display: flex;
    justify-content: flex-end;
    align-items: center;
    gap: 10px;
    height: 27px;
  }
  .contact-icon {
    width: 18px;
    height: 18px;
    flex: none;
  }
  .address {
    position: absolute;
    left: 34px;
    bottom: 26px;
    display: flex;
    align-items: center;
    gap: 8px;
    color: var(--text-soft);
    font-size: 15px;
    letter-spacing: 0.5px;
    text-transform: uppercase;
  }
  .pin-icon { width: 14px; height: 18px; }
</style>
</head>
<body>

<section class="card card-front">
  <div class="droplet-photo" role="img" aria-label="Black and white macro photograph of water droplets resting on a leaf edge"></div>
  <div class="front-monogram">DH</div>
</section>

<section class="card card-back">
  <div class="back-surface"></div>
  <div class="back-monogram">DH</div>

  <h1 class="studio-name">
    <span class="line-one">Dorian Hallet</span>
    <span class="line-two">Photography</span>
  </h1>

  <ul class="contact-list">
    <li>(555) 555-0148
      <svg class="contact-icon" viewBox="0 0 18 18" aria-hidden="true">
        <circle cx="9" cy="9" r="9" fill="var(--paper-white)"/>
        <path d="M6 4.5c.6 0 1.4 1.6 1.4 2.1 0 .5-.8.8-.8 1.2.2.9 1.5 2.3 2.4 2.5.4 0 .7-.8 1.2-.8.5 0 2.1.8 2.1 1.4 0 .8-1 1.6-1.8 1.6C7.6 12.5 5.5 10.4 5 7.5c-.1-1.1.4-3 1-3z" fill="var(--ink-dark)"/>
      </svg>
    </li>
    <li>dorian@dorianhallet.com
      <svg class="contact-icon" viewBox="0 0 18 18" aria-hidden="true">
        <circle cx="9" cy="9" r="9" fill="var(--paper-white)"/>
        <rect x="4.5" y="6" width="9" height="6.5" fill="var(--ink-dark)"/>
        <path d="M4.5 6l4.5 3.6L13.5 6" stroke="var(--paper-white)" stroke-width="0.9" fill="none"/>
      </svg>
    </li>
    <li>www.dorianhallet.com
      <svg class="contact-icon" viewBox="0 0 18 18" aria-hidden="true">
        <circle cx="9" cy="9" r="9" fill="var(--paper-white)"/>
        <circle cx="8" cy="8" r="3" stroke="var(--ink-dark)" stroke-width="1.5" fill="none"/>
        <path d="M10.2 10.2l3 3" stroke="var(--ink-dark)" stroke-width="1.7" stroke-linecap="round"/>
      </svg>
    </li>
    <li>CP:halletphoto
      <svg class="contact-icon" viewBox="0 0 18 18" aria-hidden="true">
        <circle cx="9" cy="9" r="9" fill="var(--paper-white)"/>
      </svg>
    </li>
  </ul>

  <p class="address">
    <svg class="pin-icon" viewBox="0 0 14 18" aria-hidden="true">
      <path d="M7 0C3.4 0 .8 2.6.8 6c0 4.3 6.2 12 6.2 12s6.2-7.7 6.2-12C13.2 2.6 10.6 0 7 0z" fill="var(--paper-white)"/>
      <circle cx="7" cy="6" r="2.3" fill="var(--ink-black)"/>
    </svg>
    728 Maple Brook CT, Cedar Hollow, NC 28999
  </p>
</section>

</body>
</html>
```